Business Cards and Stationery for Background Check Company
Bluepine Tenant Vetting
Business Cards and Stationery for Background Check Company - Corporate Services
Creative Brief
Use same font as used in my logo
if you choose a different font from logo, please make sure it blends well
Professional
RK Delacroix
President
2745 S. Harrow Mill Ste 300 Southlake, TX 76094
888-417-6093 ext 342
rk@bluepinevet.com
www.bluepinevet.com
front side of the card - please use the white, black, gray, with red check
on the back side, please make the entire back of the card black and use the reverse logo
Concepts
Business Cards and Stationery for new compliance company.

```html
<!DOCTYPE html>
<html lang="en">
<head>
<meta charset="utf-8">
<title>Bluepine Tenant Vetting – Business Card</title>
<link href="https://fonts.googleapis.com/css2?family=Montserrat:wght@400;500;600;700&display=swap" rel="stylesheet">
<style>
  :root {
    --bg: #d9d9d9;
    --card-white: #f7f7f7;
    --charcoal: #343434;
    --graphite: #505050;
    --mid-gray: #6e6e6e;
    --light-gray: #9a9a9a;
    --red: #e8262b;
    --ink: #3a3a3a;
  }
  * { box-sizing: border-box; margin: 0; padding: 0; }
  html, body { width: 1200px; height: 949px; overflow: hidden; }
  body {
    background: radial-gradient(ellipse at 50% 45%, #ededed 0%, var(--bg) 75%);
    font-family: "Montserrat", sans-serif;
    position: relative;
  }
  .card {
    position: absolute;
    width: 620px;
    height: 350px;
    border-radius: 14px;
    overflow: hidden;
    box-shadow: 0 14px 30px rgba(0,0,0,0.22);
  }

  /* Back */
  .card--back { left: 330px; top: 70px; background: var(--charcoal); }
  .card--back .edge-band {
    position: absolute; right: 0; top: 0; width: 40px; height: 100%;
    background: var(--mid-gray);
  }
  .edge-band .accent { position: absolute; left: 0; width: 100%; height: 70px; background: var(--red); }
  .edge-band .accent--top { top: 0; }
  .edge-band .accent--bottom { bottom: 0; }
  .card--back .brand {
    position: absolute; left: 60px; top: 156px;
    display: flex; align-items: center; gap: 12px;
  }
  .brand-name {
    font-weight: 600; font-size: 22px; letter-spacing: 1px; text-transform: uppercase;
  }
  .card--back .brand-name { color: #ffffff; }
  .brand-mark { width: 18px; height: 18px; border-radius: 50%; background: var(--red); flex: none; }
  .social-panel {
    position: absolute; right: 40px; bottom: 0; width: 200px; height: 96px;
    background: var(--graphite);
    display: flex; flex-direction: column; justify-content: center; padding-left: 26px; gap: 12px;
  }
  .social-panel .label { color: #fff; font-size: 15px; font-weight: 500; letter-spacing: 1px; }
  .social-icons { display: flex; gap: 12px; }
  .social-icons span { width: 20px; height: 20px; border-radius: 4px; background: #ffffff; }

  /* Front */
  .card--front { left: 290px; top: 500px; background: var(--card-white); }
  .card--front .edge-band {
    position: absolute; right: 0; top: 0; width: 40px; height: 100%;
    background: var(--graphite);
  }
  .card--front .brand { position: absolute; left: 40px; top: 40px; display: flex; align-items: center; gap: 12px; }
  .card--front .brand-name { color: var(--ink); }
  .person { position: absolute; left: 40px; top: 104px; }
  .person-name { color: var(--red); font-size: 25px; font-weight: 600; letter-spacing: 0.5px; text-transform: uppercase; }
  .person-title { color: var(--red); font-size: 15px; font-weight: 500; margin-top: 2px; }
  .contact-list { position: absolute; left: 40px; top: 176px; list-style: none; display: flex; flex-direction: column; gap: 9px; }
  .contact-list li { display: flex; align-items: center; gap: 12px; color: var(--ink); font-size: 13px; }
  .icon-ring {
    width: 26px; height: 26px; border-radius: 50%; border: 1.5px solid var(--red);
    display: flex; align-items: center; justify-content: center; flex: none;
  }
  .icon-ring svg { width: 14px; height: 14px; fill: var(--ink); }
  .address-bar {
    position: absolute; right: 40px; bottom: 0; width: 250px; height: 86px;
    background: var(--charcoal); color: #fff;
    display: flex; align-items: center; gap: 14px; padding: 0 18px;
    font-size: 13px; line-height: 1.45;
  }
  .pin-badge {
    width: 34px; height: 34px; border-radius: 50%; background: #fff; flex: none;
    display: flex; align-items: center; justify-content: center;
  }
  .pin-badge svg { width: 16px; height: 16px; fill: var(--charcoal); }
</style>
</head>
<body>

  <section class="card card--back" aria-label="Card back">
    <div class="edge-band"><span class="accent accent--top"></span><span class="accent accent--bottom"></span></div>
    <div class="brand">
      <span class="brand-name">Bluepine Tenant Vetting</span>
      <span class="brand-mark"></span>
    </div>
    <div class="social-panel">
      <span class="label">follow us on:</span>
      <div class="social-icons" aria-hidden="true"><span></span><span></span><span></span><span></span></div>
    </div>
  </section>

  <section class="card card--front" aria-label="Card front">
    <div class="edge-band"><span class="accent accent--top"></span><span class="accent accent--bottom"></span></div>
    <div class="brand">
      <span class="brand-name">Bluepine Tenant Vetting</span>
      <span class="brand-mark"></span>
    </div>
    <div class="person">
      <p class="person-name">RK Delacroix</p>
      <p class="person-title">President</p>
    </div>
    <ul class="contact-list">
      <li><span class="icon-ring"><svg viewBox="0 0 24 24"><path d="M6.6 10.8c1.4 2.8 3.8 5.1 6.6 6.6l2.2-2.2c.3-.3.7-.4 1-.2 1.1.4 2.3.6 3.6.6.6 0 1 .4 1 1V20c0 .6-.4 1-1 1C10.6 21 3 13.4 3 4c0-.6.4-1 1-1h3.5c.6 0 1 .4 1 1 0 1.3.2 2.5.6 3.6.1.3 0 .7-.2 1z"/></svg></span>888-417-6093 ext 342</li>
      <li><span class="icon-ring"><svg viewBox="0 0 24 24"><path d="M7 2h10a2 2 0 0 1 2 2v16a2 2 0 0 1-2 2H7a2 2 0 0 1-2-2V4a2 2 0 0 1 2-2zm0 3v13h10V5zm5 14.2a1 1 0 1 0 0 .01z"/></svg></span>888-417-6093</li>
      <li><span class="icon-ring"><svg viewBox="0 0 24 24"><path d="M3 5h18v14H3zm2 2v.5l7 4.5 7-4.5V7zm0 3v7h14v-7l-7 4.5z"/></svg></span>rk@bluepinevet.com</li>
      <li><span class="icon-ring"><svg viewBox="0 0 24 24"><path d="M12 2a10 10 0 1 0 0 20 10 10 0 0 0 0-20zm7.9 9h-3.4a15 15 0 0 0-1.3-5.9A8 8 0 0 1 19.9 11zM12 4c1 1.3 2.3 3.9 2.5 7h-5C9.7 7.9 11 5.3 12 4zM8.8 5.1A15 15 0 0 0 7.5 11H4.1a8 8 0 0 1 4.7-5.9zM4.1 13h3.4a15 15 0 0 0 1.3 5.9A8 8 0 0 1 4.1 13zM12 20c-1-1.3-2.3-3.9-2.5-7h5c-.2 3.1-1.5 5.7-2.5 7zm3.2-1.1a15 15 0 0 0 1.3-5.9h3.4a8 8 0 0 1-4.7 5.9z"/></svg></span>www.bluepinevet.com</li>
    </ul>
    <div class="address-bar">
      <span class="pin-badge"><svg viewBox="0 0 24 24"><path d="M12 2a7 7 0 0 0-7 7c0 5.2 7 13 7 13s7-7.8 7-13a7 7 0 0 0-7-7zm0 9.5a2.5 2.5 0 1 1 0-5 2.5 2.5 0 0 1 0 5z"/></svg></span>
      <p>2745 S. Harrow Mill Ste 300<br>Southlake, TX 76094</p>
    </div>
  </section>

</body>
</html>
```